National Virtual CPA Firm needs post card design

Virtual CPA firm called "BRELLVO" needs a 5.5” x 8.5” post card designed to market our services to middle market mid-size american businesses. We provide Full Service Payroll (includes the processing of payroll, printing of checks and direct depositing, tax filing, and tax payments), Bookkeeping (Using their native systems, or ours), Contract CFO (with expense reduction analysis), Reporting services for business directors to make informed decisions, Capital Fundraising (Advice on seeking equity to help grow your business), and Taxes (Personal (1040), Partnership (1065), Corporate (1120, 1120S (Including Consolidated Returns)), Trust (1041) and Non-Profit (990)), including all affiliated state returns. One of our major selling points is our variety of experience, and our fast turn around times on projects.
This project specifically, I would like to highlight the bookkeeping services, but still want the tax and payroll services listed on the postcard.
I have uploaded the logo design for BRELLVO and would like a postcard that compliments the logo.
Company contact info is:
Brellvo accounting services Inc
P.O. Box 4638
Harlow Springs, NV 59172
(800) 613-2794
Www.brellvo-example.com
Target Market(s)
Small to medium size businesses
Industry/Entity Type
Accounting
Look and feel

```html
<!DOCTYPE html>
<html lang="en">
<head>
<meta charset="utf-8">
<title>Brellvo Postcard</title>
<link rel="stylesheet" href="https://fonts.googleapis.com/css2?family=Montserrat:wght@400;500;600;700;800&display=swap">
<style>
  :root {
    --stage: #d9d9d9;
    --green: #4cb848;
    --green-text: #5bbd2b;
    --yellow: #f5c518;
    --yellow-fill: #fdd41e;
    --dark: #414141;
    --ink: #1d1d1d;
    --paper-top: #e4e4e4;
    --paper: #fbfbfb;
  }
  * { box-sizing: border-box; margin: 0; padding: 0; }
  html, body { width: 720px; height: 1200px; overflow: hidden; }
  body {
    background: var(--stage);
    font-family: "Montserrat", sans-serif;
    color: var(--ink);
    position: relative;
  }
  .card {
    position: absolute;
    left: 20px;
    width: 680px;
    height: 440px;
    overflow: hidden;
    box-shadow: 0 6px 18px rgba(0,0,0,.28);
    background: linear-gradient(180deg, var(--paper-top) 0%, var(--paper) 45%, #ffffff 100%);
  }
  .card--front { top: 110px; }
  .card--back { top: 620px; }
  .card__art { position: absolute; inset: 0; }

  .brand {
    position: absolute;
    display: flex;
    align-items: center;
    gap: 10px;
    font-weight: 800;
    color: var(--ink);
    letter-spacing: .5px;
  }
  .brand__dot {
    width: 22px; height: 22px; border-radius: 50%;
    background: var(--yellow);
  }
  .card--front .brand { left: 38px; top: 44px; font-size: 34px; }
  .card--back .brand { right: 28px; top: 36px; font-size: 27px; }
  .card--back .brand__dot { width: 18px; height: 18px; }

  .payroll {
    position: absolute;
    left: 300px; top: 22px;
    width: 370px;
    text-align: center;
    font-size: 15.5px;
    line-height: 23.5px;
    font-weight: 500;
  }
  .payroll strong { font-weight: 700; }
  .hl { color: var(--green-text); font-weight: 700; }

  .services {
    position: absolute;
    left: 368px; top: 196px;
    list-style: none;
    color: #fff;
  }
  .services li { position: relative; padding-left: 25px; margin-bottom: 11px; }
  .services h3 {
    color: var(--yellow);
    font-size: 18.5px;
    font-weight: 700;
    line-height: 22px;
  }
  .services p { font-size: 13.5px; line-height: 16px; width: 260px; }
  .tick { position: absolute; left: 0; top: 3px; width: 16px; height: 16px; }

  .returns { position: absolute; left: 0; top: 0; list-style: none; }
  .returns li { position: absolute; padding-left: 18px; white-space: nowrap; }
  .returns h3 { color: var(--green-text); font-size: 15.5px; font-weight: 700; line-height: 18px; }
  .returns p { font-size: 11px; line-height: 13.5px; }
  .returns .tick { width: 12px; height: 12px; top: 3px; }

  .pitch {
    position: absolute;
    left: 45px; top: 143px;
    width: 420px;
    font-size: 11px;
    line-height: 13.5px;
    font-weight: 500;
  }

  .contact {
    position: absolute;
    left: 23px; top: 311px;
    font-size: 11px;
    font-weight: 700;
    font-style: normal;
    line-height: 13.5px;
    color: var(--ink);
  }
  .contact p { margin-bottom: 11px; }
</style>
</head>
<body>

<section class="card card--front">
  <svg class="card__art" viewBox="0 0 680 440" width="680" height="440">
    <defs>
      <clipPath id="front-dark-clip">
        <path d="M0,210 C40,165 130,150 300,150 C470,150 600,182 680,202 L680,440 L0,440 Z"/>
      </clipPath>
      <radialGradient id="meeting-tones" cx="0.42" cy="0.55" r="0.65">
        <stop offset="0" stop-color="#8a7d70"/>
        <stop offset="0.45" stop-color="#5e5650"/>
        <stop offset="1" stop-color="#414141" stop-opacity="0"/>
      </radialGradient>
    </defs>
    <path d="M0,200 C35,145 120,128 300,130 C470,132 600,170 680,198 L680,440 L0,440 Z" fill="var(--green)"/>
    <path d="M0,210 C40,165 130,150 300,150 C470,150 600,182 680,202 L680,440 L0,440 Z" fill="var(--dark)"/>
    <g clip-path="url(#front-dark-clip)" role="img" aria-label="Photo from above of business people at a round table working on a laptop, calculator and notebook">
      <rect x="0" y="140" width="400" height="300" fill="url(#meeting-tones)"/>
    </g>
  </svg>

  <div class="brand"><span class="brand__dot"></span>BRELLVO</div>

  <p class="payroll">We provide <strong>FULL SERVICE PAYROLL</strong> (includes the processing of <span class="hl">PAYROLL</span>, <span class="hl">PRINTING</span> of <span class="hl">CHECKS</span> and <span class="hl">DIRECT DEPOSITING</span>, <strong>TAX FILING</strong>, and <span class="hl">TAX PAYMENTS</span>),</p>

  <ul class="services">
    <li>
      <svg class="tick" viewBox="0 0 16 16"><circle cx="8" cy="8" r="6.3" fill="none" stroke="var(--green)" stroke-width="1.8"/><path d="M4.8 8.2l2.3 2.3 5.5-6" fill="none" stroke="var(--green)" stroke-width="2"/></svg>
      <h3>BOOKKEEPING</h3>
      <p>(Using their native systems, or ours)</p>
    </li>
    <li>
      <svg class="tick" viewBox="0 0 16 16"><circle cx="8" cy="8" r="6.3" fill="none" stroke="var(--green)" stroke-width="1.8"/><path d="M4.8 8.2l2.3 2.3 5.5-6" fill="none" stroke="var(--green)" stroke-width="2"/></svg>
      <h3>CONTRACT CFO</h3>
      <p>(with expense reduction analysis)</p>
    </li>
    <li>
      <svg class="tick" viewBox="0 0 16 16"><circle cx="8" cy="8" r="6.3" fill="none" stroke="var(--green)" stroke-width="1.8"/><path d="M4.8 8.2l2.3 2.3 5.5-6" fill="none" stroke="var(--green)" stroke-width="2"/></svg>
      <h3>REPORTING SERVICES</h3>
      <p>(for business directors to make informed decisions)</p>
    </li>
    <li>
      <svg class="tick" viewBox="0 0 16 16"><circle cx="8" cy="8" r="6.3" fill="none" stroke="var(--green)" stroke-width="1.8"/><path d="M4.8 8.2l2.3 2.3 5.5-6" fill="none" stroke="var(--green)" stroke-width="2"/></svg>
      <h3>CAPITAL FUNDRAISING</h3>
      <p>(Advice on seeking equity to help grow your business)</p>
    </li>
  </ul>
</section>

<section class="card card--back">
  <svg class="card__art" viewBox="0 0 680 440" width="680" height="440">
    <defs>
      <linearGradient id="desk-tones" x1="0" y1="0" x2="1" y2="1">
        <stop offset="0" stop-color="#f4f4f4"/>
        <stop offset="0.5" stop-color="#e2dfda"/>
        <stop offset="1" stop-color="#c9c6c2"/>
      </linearGradient>
      <linearGradient id="desk-fade" x1="0" y1="0" x2="0" y2="1">
        <stop offset="0" stop-color="#fff" stop-opacity="0"/>
        <stop offset="0.25" stop-color="#fff" stop-opacity="1"/>
      </linearGradient>
      <mask id="desk-mask"><rect x="0" y="175" width="680" height="265" fill="url(#desk-fade)"/></mask>
    </defs>
    <rect role="img" aria-label="Photo from above of a desk with a laptop showing charts, a calculator, coffee cup, plant, notes and hands holding a phone" x="110" y="175" width="570" height="265" fill="url(#desk-tones)" mask="url(#desk-mask)"/>
    <circle cx="60" cy="440" r="186" fill="none" stroke="var(--green)" stroke-width="1"/>
    <circle cx="52" cy="446" r="180" fill="var(--yellow-fill)"/>
  </svg>

  <div class="brand"><span class="brand__dot"></span>BRELLVO</div>

  <ul class="returns">
    <li style="left:26px;top:22px">
      <svg class="tick" viewBox="0 0 16 16"><circle cx="8" cy="8" r="6.3" fill="none" stroke="var(--yellow)" stroke-width="1.8"/><path d="M4.8 8.2l2.3 2.3 5.5-6" fill="none" stroke="var(--green)" stroke-width="2"/></svg>
      <h3>TAXES</h3><p>(Personal (1040)</p>
    </li>
    <li style="left:194px;top:22px">
      <svg class="tick" viewBox="0 0 16 16"><circle cx="8" cy="8" r="6.3" fill="none" stroke="var(--yellow)" stroke-width="1.8"/><path d="M4.8 8.2l2.3 2.3 5.5-6" fill="none" stroke="var(--green)" stroke-width="2"/></svg>
      <h3>CORPORATE</h3><p>(1120, 1120S<br>(Including Consolidated Returns))</p>
    </li>
    <li style="left:26px;top:87px">
      <svg class="tick" viewBox="0 0 16 16"><circle cx="8" cy="8" r="6.3" fill="none" stroke="var(--yellow)" stroke-width="1.8"/><path d="M4.8 8.2l2.3 2.3 5.5-6" fill="none" stroke="var(--green)" stroke-width="2"/></svg>
      <h3>PARTNERSHIP</h3><p>(1065)</p>
    </li>
    <li style="left:194px;top:87px">
      <svg class="tick" viewBox="0 0 16 16"><circle cx="8" cy="8" r="6.3" fill="none" stroke="var(--yellow)" stroke-width="1.8"/><path d="M4.8 8.2l2.3 2.3 5.5-6" fill="none" stroke="var(--green)" stroke-width="2"/></svg>
      <h3>TRUST</h3><p>(1041)</p>
    </li>
    <li style="left:316px;top:87px">
      <svg class="tick" viewBox="0 0 16 16"><circle cx="8" cy="8" r="6.3" fill="none" stroke="var(--yellow)" stroke-width="1.8"/><path d="M4.8 8.2l2.3 2.3 5.5-6" fill="none" stroke="var(--green)" stroke-width="2"/></svg>
      <h3>NON-PROFIT</h3><p>(990)</p>
    </li>
  </ul>

  <p class="pitch">One of our major selling points is our variety of experience, and our fast turn around times on projects.</p>

  <address class="contact">
    <p>BRELLVO ACCOUNTING<br>SERVICES INC</p>
    <p>P.O. Box 4638<br>Harlow Springs, NV 59172</p>
    <p>(800) 613-2794</p>
    <p>Www.brellvo-example.com</p>
  </address>
</section>

</body>
</html>
```